Company Real Estate Site Needs A Face Lift

I need a new website for the recent company I formed: Voska Real Estate.
You can use my agent website WWW.PALMIROQ.COM to see the style/brand I already have. I will have areas for Searching for homes on IDX, etc.
I really like this site:
http://www.cranfeltmanorhomes.com/
I have attached my logo as well

Industry/Entity Type

Real Estate

Colors
0255a3
ffffff
cee9f5

```html
<!DOCTYPE html>
<html lang="en">
<head>
<meta charset="utf-8">
<title>Voska Real Estate</title>
<link rel="stylesheet" href="https://fonts.googleapis.com/css2?family=Questrial&family=Open+Sans:wght@400;600;700&family=Arimo:wght@400;700&display=swap">
<style>
:root{
  --brand-blue:#0255a3;
  --stripe-blue:#0660d6;
  --ice:#cee9f5;
  --white:#ffffff;
  --ink:#1a1a1a;
  --body-grey:#444444;
  --metal-dark:#9c9c9c;
  --metal-light:#dcdcdc;
  --footer:#222222;
  --footer-text:#8a8a8a;
}
*{margin:0;padding:0;box-sizing:border-box}
html,body{width:1200px;height:754px;overflow:hidden;background:var(--white)}
.page{position:relative;width:1200px;height:754px;overflow:hidden;font-family:"Arimo",Arial,sans-serif}

/* top navigation */
.main-nav{position:absolute;left:0;top:0;width:1200px;height:43px;
  background:linear-gradient(#ffffff 0%,#f7f7f7 50%,#ececec 100%);border-bottom:1px solid #cfcfcf}
.main-nav a{position:absolute;top:12px;font-family:"Questrial",sans-serif;font-size:13.5px;color:#333;
  text-decoration:none;transform:translateX(-50%);letter-spacing:.2px}
.main-nav a.is-active{top:7px;left:187px;width:65px;height:25px;line-height:25px;text-align:center;
  background:var(--brand-blue);color:var(--white);border-radius:3px}
.nav-sep{position:absolute;top:10px;width:1px;height:26px;background:#c8c8c8}

/* header */
.site-header{position:absolute;left:0;top:43px;width:1200px;height:95px;
  background:linear-gradient(180deg,#a9a9a9 0%,#d9d9d9 45%,#c4c4c4 75%,#8e8e8e 100%)}
.brand{position:absolute;left:140px;top:14px;color:var(--white);font-family:"Questrial",sans-serif;text-align:center}
.brand-name{display:block;font-size:44px;line-height:44px;letter-spacing:2px}
.brand-sub{display:block;font-size:13px;letter-spacing:5.5px;margin-top:2px}
.phone-icon{position:absolute;left:568px;top:19px}
.phone-number{position:absolute;left:620px;top:30px;font-family:"Questrial",sans-serif;font-size:25px;color:var(--white)}
.header-sep{position:absolute;left:815px;top:22px;width:1px;height:50px;background:#8f8f8f;box-shadow:1px 0 0 #e6e6e6}
.join-label{position:absolute;left:840px;top:31px;font-family:"Questrial",sans-serif;font-size:23px;color:var(--white)}
.social{position:absolute;top:24px;width:42px;height:42px;border-radius:50%}
.social-a{left:945px;background:var(--brand-blue)}
.social-b{left:1006px;background:#e9e9e9}

/* hero */
.hero-photo{position:absolute;left:0;top:138px;width:1200px;height:422px;
  background:linear-gradient(180deg,#4f86d4 0%,#8fb6e8 14%,#a39484 30%,#8c7a68 55%,#b9ada0 72%,#3f79b8 88%,#2d5f9a 100%)}
.stripe{position:absolute;left:0;top:0;width:1200px;height:754px;pointer-events:none}
.welcome-panel{position:absolute;left:0;top:0;width:1200px;height:754px;pointer-events:none}
.welcome-copy{position:absolute;left:346px;top:242px;width:312px}
.welcome-title{font-family:"Questrial",sans-serif;font-weight:400;font-size:30px;line-height:34px;color:var(--ink)}
.welcome-title strong{color:var(--brand-blue);font-family:"Arimo",Arial,sans-serif;font-weight:700}
.welcome-lead{margin-top:9px;font-size:12px;line-height:18.5px;color:var(--body-grey)}
.welcome-note{margin-top:5px;font-size:12.5px;line-height:18px;font-weight:700;color:#111;width:295px}
.cta-link{position:absolute;left:452px;top:424px;font-size:12.5px;font-weight:700;color:var(--brand-blue);text-decoration:none}

/* lower band */
.feature-band{position:absolute;left:0;top:560px;width:1200px;height:164px;
  background:linear-gradient(180deg,#a7a7a7 0%,#d6d6d6 40%,#c9c9c9 70%,#a0a0a0 100%)}
.feature-sep{position:absolute;left:649px;top:12px;width:1px;height:140px;background:#9a9a9a;box-shadow:1px 0 0 #e2e2e2}
.feature{position:absolute;top:18px;width:340px;font-family:"Open Sans",sans-serif}
.feature-news{left:284px}
.feature-events{left:690px}
.feature h2{font-size:21px;font-weight:700;color:var(--white);line-height:26px;text-shadow:0 1px 2px rgba(0,0,0,.45)}
.feature h3{margin-top:5px;font-size:12.5px;font-weight:700;color:var(--brand-blue);line-height:18px}
.feature p{margin-top:2px;font-size:12px;line-height:17px;color:#111}
.more-btn{display:inline-block;margin-top:9px;height:23px;line-height:23px;padding:0 14px 0 6px;font-size:12px;color:#111;
  text-decoration:none;background:var(--white);clip-path:polygon(0 0,100% 0,92% 100%,0 100%)}

/* footer */
.site-footer{position:absolute;left:0;top:724px;width:1200px;height:30px;background:var(--footer);
  text-align:center;padding-left:166px;font-size:13px;line-height:30px;color:var(--footer-text)}
</style>
</head>
<body>
<div class="page">

  <nav class="main-nav">
    <a class="is-active" href="#">HOME</a>
    <span class="nav-sep" style="left:247px"></span>
    <a href="#" style="left:301px">AUCTIONS</a>
    <span class="nav-sep" style="left:369px"></span>
    <a href="#" style="left:429px">SERVICES</a>
    <span class="nav-sep" style="left:492px"></span>
    <a href="#" style="left:555px">FOR SALE</a>
    <span class="nav-sep" style="left:621px"></span>
    <a href="#" style="left:681px">ABOUT US</a>
    <span class="nav-sep" style="left:747px"></span>
    <a href="#" style="left:801px">EVENTS</a>
    <span class="nav-sep" style="left:858px"></span>
    <a href="#" style="left:928px">CONTACT US</a>
  </nav>

  <header class="site-header">
    <div class="brand">
      <span class="brand-name">VOSKA</span>
      <span class="brand-sub">REAL ESTATE</span>
    </div>
    <svg class="phone-icon" width="32" height="46" viewBox="0 0 32 46" aria-hidden="true">
      <rect x="4" y="2" width="22" height="42" rx="4" fill="#1c1c1c" transform="rotate(-12 15 23)"/>
      <rect x="7" y="8" width="16" height="26" rx="1" fill="#1f86e6" transform="rotate(-12 15 23)"/>
    </svg>
    <span class="phone-number">1-800-555-0187</span>
    <span class="header-sep"></span>
    <span class="join-label">Join Us:</span>
    <a class="social social-a" href="#" aria-label="Social network page"></a>
    <a class="social social-b" href="#" aria-label="Video channel"></a>
  </header>

  <div class="hero-photo" role="img" aria-label="Photograph of a modern stucco home with pool, patio seating and desert plants"></div>

  <svg class="stripe" viewBox="0 0 1200 754" aria-hidden="true">
    <polygon points="318,43 397,43 231,724 152,724" fill="var(--stripe-blue)"/>
    <polygon points="295,138 372,138 370,146 293,146" fill="#0a3f8a"/>
  </svg>

  <svg class="welcome-panel" viewBox="0 0 1200 754" aria-hidden="true">
    <polygon points="268,226 729,226 605,485 210,485" fill="#ffffff" fill-opacity=".9"/>
    <polygon points="268,226 350,226 290,485 210,485" fill="var(--ice)" fill-opacity=".5"/>
  </svg>

  <section class="welcome-copy">
    <h1 class="welcome-title">Welcome To <strong>VOSKA</strong></h1>
    <p class="welcome-lead">Corrupti quos dolores et quas molestias dignissimos duci-mus qui blanditiis praesentium voluptatum deleniti atque corrupti quos dolores et quas molestias excepturi sint occaecati cupiditate non provident, simi</p>
    <p class="welcome-note">At vero eos et accusamus et iusto odio dignissi-mos ducimus qui blanditiis praesentium</p>
  </section>
  <a class="cta-link" href="#">List your Property Now ›</a>

  <section class="feature-band">
    <span class="feature-sep"></span>
    <article class="feature feature-news">
      <h2>LATEST NEWS</h2>
      <h3>Lorem Ipsum is simply dummy printing&nbsp; typesetting.</h3>
      <p>when an unknown printer took a galley of type and scra mbled it to make type specimen book.</p>
      <a class="more-btn" href="#">More Info ››</a>
    </article>
    <article class="feature feature-events">
      <h2>LATEST EVENTS</h2>
      <h3>Lorem Ipsum is simply dummy printing&nbsp; typesetting.</h3>
      <p>when an unknown printer took a galley of type and scra mbled it to make type specimen book.</p>
      <a class="more-btn" href="#">More Info ››</a>
    </article>
  </section>

  <svg class="stripe" viewBox="0 0 1200 754" aria-hidden="true">
    <polygon points="185,560 264,560 231,724 152,724" fill="var(--stripe-blue)"/>
  </svg>

  <footer class="site-footer">© 2014 Copyright - Voska Real Estate . All rights reserved</footer>
</div>
</body>
</html>
```